K7Q480 brochure

We want a new brochure for our rebranding of our sports health and wellness centre. We are based in Townsville in North Queensland. We provide chiropractic, physiotherapy, massage, nutrition and yoga services. We would like to see designs and content that portray our unique one stop destination for many allied health services and our one on one functional rehab approach customised to each individual. We would like to keep colours that compliment our logo colours. The design should be professional and one that could be handed out to Medical Doctors, other referring healthcare professionals and prospective sports and active lifestyle patients. The brochure should also note that we also accept/treat Jobshield, RSB, Vitafund KPS, and Accident and Injury referrals
Updates

Please check out our website for more information on who we are and what we do. I will upload our new logo in a few moments. Cheers! Www.peakvitaro.com.au

Reason: We understand creating a quality brochure takes time and we wanted to give the creatives more time to create. With the extended deadline we are now guaranteeing the payment.

Target Market(s)

Referring Medical Doctors and other health professionals
Athletes and Active lifestyle patients
Wellness patients

Industry/Entity Type

Healthcare

Requirements
Nice to have
• Brochure can be single double sided, or bi-fold of approx. size of 210mm x 99mm
Should not have
• Brochure should not focus on or place emphasis on one particular service that we offer rather focus on the services provided as a whole.

```html
<!DOCTYPE html>
<html lang="en">
<head>
<meta charset="utf-8">
<title>K7Q480 Brochure Cover</title>
<link href="https://fonts.googleapis.com/css2?family=Roboto+Condensed:ital,wght@0,400;0,700;1,400&display=swap" rel="stylesheet">
<style>
  :root {
    --page: #ffffff;
    --red: #e41e26;
    --red-dark: #8c1116;
    --blue: #0f3f8c;
    --shade: #1a0a0c;
    --white: #ffffff;
  }
  html, body {
    margin: 0;
    width: 1200px;
    height: 848px;
    overflow: hidden;
    background: var(--page);
    font-family: "Roboto Condensed", "Arial Narrow", sans-serif;
  }
  .brochure {
    position: absolute;
    left: 176px;
    top: 224px;
    width: 848px;
    height: 400px;
    overflow: hidden;
    background: var(--red);
  }
  .brochure svg.backdrop {
    position: absolute;
    inset: 0;
  }
  .brand {
    position: absolute;
    left: 112px;
    top: 196px;
    color: var(--white);
  }
  .brand-name {
    font-weight: 700;
    font-size: 40px;
    line-height: 1;
    letter-spacing: 0.5px;
  }
  .brand-tagline {
    font-size: 14px;
    letter-spacing: 1.5px;
    margin-top: 2px;
  }
  .brand-url {
    font-style: italic;
    font-size: 16px;
    margin-top: 4px;
    padding-left: 40px;
  }
  .headline {
    position: absolute;
    left: 470px;
    top: 84px;
    width: 340px;
    color: var(--white);
    font-weight: 700;
    text-align: center;
    transform: rotate(-8deg);
    transform-origin: center;
  }
  .headline-lead {
    font-size: 23px;
    line-height: 1;
  }
  .headline-key {
    font-size: 68px;
    line-height: 0.95;
    letter-spacing: 0.5px;
  }
  .services {
    position: absolute;
    left: 530px;
    top: 238px;
    width: 270px;
    color: var(--white);
    text-align: center;
    transform: rotate(-8deg);
  }
  .services-intro {
    font-size: 16px;
    margin-bottom: 2px;
  }
  .services-list {
    font-weight: 700;
    font-size: 21px;
    line-height: 1.05;
  }
</style>
</head>
<body>
  <section class="brochure">
    <svg class="backdrop" width="848" height="400" viewBox="0 0 848 400">
      <defs>
        <radialGradient id="athlete-left" cx="0.5" cy="0.5" r="0.5">
          <stop offset="0" stop-color="#1a0a0c" stop-opacity="0.8"/>
          <stop offset="1" stop-color="#1a0a0c" stop-opacity="0"/>
        </radialGradient>
        <radialGradient id="athlete-right" cx="0.5" cy="0.5" r="0.5">
          <stop offset="0" stop-color="#2a0a0e" stop-opacity="0.75"/>
          <stop offset="1" stop-color="#2a0a0e" stop-opacity="0"/>
        </radialGradient>
      </defs>
      <!-- left panel bands -->
      <polygon class="band-top" points="0,78 424,28 424,128 0,180" fill="var(--blue)"/>
      <polygon points="0,180 424,128 424,134 0,186" fill="var(--red-dark)"/>
      <polygon class="band-bottom" points="0,372 424,322 424,400 0,400" fill="var(--blue)"/>
      <polygon points="0,366 424,316 424,322 0,372" fill="var(--red-dark)"/>
      <!-- right panel headline band -->
      <polygon class="band-headline" points="424,128 848,70 848,150 424,208" fill="var(--blue)"/>
      <polygon points="424,208 848,150 848,170 424,228" fill="var(--shade)" opacity="0.55"/>
      <!-- athlete photo areas -->
      <rect role="img" aria-label="Photo of a sprinting athlete in motion" x="110" y="0" width="330" height="400" fill="url(#athlete-left)"/>
      <rect role="img" aria-label="Photo of an athlete sprinting towards the viewer" x="420" y="0" width="428" height="400" fill="url(#athlete-right)"/>
      <line x1="424" y1="0" x2="424" y2="400" stroke="var(--shade)" stroke-opacity="0.35" stroke-width="2"/>
    </svg>

    <div class="brand">
      <div class="brand-name">K7Q480</div>
      <div class="brand-tagline">Sports Health and Wellness</div>
      <div class="brand-url">www.peakvitaro.com.au</div>
    </div>

    <div class="headline">
      <div class="headline-lead">Improve Your Wellness With An</div>
      <div class="headline-key">Adjustment</div>
    </div>

    <div class="services">
      <div class="services-intro">Proudly Providing :</div>
      <div class="services-list">Chiropractic &bull; Physiotherapy<br>Massage &bull; Nutrition &bull; Yoga</div>
    </div>
  </section>
</body>
</html>
```